Tillard Environmental Projects New Website Design

I need a new website for a Environmental Project Company based in Sydney Australia, working throughout South East Asia.I've attached the company logo, please try & incorporate these colours or use complimentary colours. I've attached a word doc with design brief.I'm going to use Wix, so please ensure files are suitable.Thankyou.

Number of Pages Required

5+ page

Colors

Designer to choose colors to be used in the design.

Requirements
Must have
• Refer to Word Document
Nice to have
• Refer to Word Document
Should not have
• Not to be dark

```html
<!DOCTYPE html>
<html lang="en">
<head>
<meta charset="utf-8">
<title>Tillard Environmental Projects</title>
<link rel="stylesheet" href="https://fonts.googleapis.com/css2?family=Cinzel:wght@400;600;700&family=Jost:wght@400;500;600&family=Arimo:wght@400&display=swap">
<style>
:root{
  --teal:#1bb191;
  --teal-dark:#149a7e;
  --forest:#4a5e24;
  --forest-dark:#3c4e1b;
  --ink:#1f2a2b;
  --text:#3a3f40;
  --muted:#777;
  --panel:#f1f2f2;
  --line:#e2e4e4;
  --white:#fff;
  --foot-bar:#1d2527;
}
*{margin:0;padding:0;box-sizing:border-box}
html,body{width:1200px;height:3651px;overflow:hidden}
body{position:relative;background:var(--white);font-family:'Jost',sans-serif;color:var(--text)}
.abs{position:absolute}

/* header */
.site-header{left:0;top:0;width:1200px;height:92px;background:var(--white)}
.nav-item{top:34px;font-size:15px;color:var(--ink)}
.nav-item.active{color:var(--teal)}
.nav-item .caret{font-size:10px;margin-left:4px}
.brand{left:452px;top:33px;display:flex;align-items:center;gap:10px}
.brand .mark{width:18px;height:18px;background:var(--forest)}
.brand .name{font-family:'Jost',sans-serif;font-weight:500;color:var(--forest);font-size:17px;white-space:nowrap}

/* hero */
.hero{left:0;top:92px;width:1200px;height:597px;background:linear-gradient(180deg,#4f7a3a 0%,#3e6b2c 35%,#5c9240 65%,#3e5f2b 100%)}
.hero-title{left:0;top:536px;width:1200px;text-align:center;font-family:'Arimo',sans-serif;font-weight:400;color:var(--white);font-size:33px;line-height:42px;text-shadow:0 2px 6px rgba(0,0,0,.45)}
.hero-dots{top:650px;left:562px;display:flex;gap:8px}
.hero-dots span{width:14px;height:14px;border-radius:50%;border:2px solid var(--white)}
.hero-dots span.on{background:var(--teal)}

/* welcome */
.welcome-title{left:0;top:775px;width:1200px;text-align:center;font-family:'Cinzel',serif;font-weight:400;font-size:26px;color:var(--ink);letter-spacing:1px}
.welcome-title em{font-style:normal;color:var(--forest)}
.welcome-lead{left:0;top:843px;width:1200px;text-align:center;font-weight:600;font-size:16px;color:var(--ink)}
.welcome-copy{left:92px;top:877px;width:1016px;text-align:center;font-size:14px;line-height:27px;color:var(--text)}
.btn{background:var(--teal);color:var(--white);font-family:'Cinzel',serif;font-size:15px;letter-spacing:1px;text-align:center}
.welcome-btn{left:528px;top:942px;width:144px;height:34px;line-height:34px}

/* mission / vision */
.mission{left:0;top:1059px;width:601px;height:343px;background:var(--forest)}
.vision{left:601px;top:1059px;width:599px;height:343px;background:var(--teal)}
.mv-head{display:flex;align-items:center;gap:12px;font-family:'Cinzel',serif;font-size:30px;color:var(--white)}
.mv-copy{font-size:14.5px;line-height:25px;color:rgba(255,255,255,.85)}
.mv-more{font-family:'Cinzel',serif;font-size:15px;color:var(--white);letter-spacing:1px}
.mv-badge{left:487px;top:1115px;width:228px;height:228px;border-radius:50%;background:var(--white);border:10px solid #dfe7e3}

/* products */
.products{left:0;top:1402px;width:1200px;height:684px;background:var(--panel)}
.section-title{font-family:'Cinzel',serif;font-weight:400;font-size:33px;color:var(--ink);letter-spacing:1px}
.product-card{top:1563px;width:316px;height:377px;background:var(--white);box-shadow:0 2px 8px rgba(0,0,0,.12);border-bottom:4px solid var(--forest)}
.product-card .pic{position:absolute;left:7px;top:7px;width:302px;height:200px}
.product-card h3{position:absolute;left:18px;top:230px;font-weight:500;font-size:20px;color:var(--ink)}
.product-card p{position:absolute;left:18px;top:280px;width:270px;font-size:12.5px;line-height:22px;color:var(--muted)}
.product-card .plus{position:absolute;left:136px;top:349px;width:44px;height:24px;border-radius:22px 22px 0 0;background:var(--forest);color:var(--white);text-align:center;font-size:22px;line-height:28px}
.slider-arrow{width:20px;height:40px}

/* projects & events */
.proj-caption{left:90px;top:2535px;width:239px;text-align:center;color:var(--white)}
.proj-caption b{display:block;font-weight:500;font-size:17px;letter-spacing:.5px}
.proj-caption span{font-size:12px;line-height:18px;opacity:.9}
.tab{top:2227px;height:27px;line-height:27px;font-size:13px;color:var(--white);text-align:center}
.event{left:623px;width:480px;height:88px;border-bottom:1px solid var(--line)}
.event .date{position:absolute;left:0;top:0;width:44px;border:1px solid var(--teal);text-align:center}
.event .date b{display:block;font-weight:400;font-size:14px;color:var(--teal);line-height:22px}
.event .date i{display:block;font-style:normal;font-size:12px;background:var(--teal);color:var(--white);line-height:20px}
.event h4{position:absolute;left:56px;top:-2px;font-weight:500;font-size:15px;color:var(--ink)}
.event p{position:absolute;left:56px;top:22px;width:420px;font-size:12.5px;line-height:20px;color:var(--muted)}

/* testimonials */
.testimonials{left:0;top:2782px;width:1200px;height:470px;background:linear-gradient(180deg,#2c4d55 0%,#3a5f63 50%,#2a4548 100%)}
.testi-title{left:0;top:2862px;width:1200px;text-align:center;font-family:'Cinzel',serif;font-weight:400;font-size:36px;color:#6f9a3c;letter-spacing:1px}
.testi-title em{font-style:normal;color:var(--teal)}
.testi-copy{left:243px;top:2940px;width:714px;text-align:center;font-size:13px;line-height:22px;color:var(--white)}
.avatar{top:3069px;width:64px;height:64px;border-radius:50%;background:#cfd4d4;border:3px solid var(--white)}
.avatar.on{border:4px solid var(--teal)}
.testi-name{left:0;top:3148px;width:1200px;text-align:center;font-family:'Cinzel',serif;font-size:16px;color:var(--white);letter-spacing:1px}

/* footer */
.site-footer{left:0;top:3252px;width:1200px;height:350px;background:var(--teal)}
.foot-head{top:3306px;font-family:'Cinzel',serif;font-weight:400;font-size:20px;color:var(--white);letter-spacing:1px}
.foot-line{left:124px;font-size:15px;color:var(--white);line-height:22px}
.foot-icon{left:90px}
.map{left:433px;top:3376px;width:307px;height:156px;background:linear-gradient(135deg,#e7e5de,#d6d9cf)}
.foot-brand{left:806px;top:3440px;display:flex;align-items:center;gap:12px}
.foot-brand .mark{width:22px;height:22px;background:var(--white)}
.foot-brand .name{font-family:'Jost',sans-serif;font-weight:500;color:var(--white);font-size:20px;white-space:nowrap}
.bottom-bar{left:0;top:3602px;width:1200px;height:49px;background:var(--foot-bar)}
.copyright{left:90px;top:15px;font-size:13px;color:#d9dcdc}
.socials{left:986px;top:16px;display:flex;gap:22px}
.socials span{width:16px;height:16px;border-radius:50%;background:var(--white)}
</style>
</head>
<body>

<header class="abs site-header">
  <div class="abs nav-item active" style="left:94px">Home
    <svg class="abs" style="left:0;top:22px" width="42" height="4"><rect width="42" height="2" fill="#1bb191"/></svg>
  </div>
  <div class="abs nav-item" style="left:190px">Who We Are<span class="caret">&#9662;</span></div>
  <div class="abs nav-item" style="left:348px">Services<span class="caret">&#9662;</span></div>
  <div class="abs brand"><span class="mark"></span><span class="name">Tillard Environmental Projects</span></div>
  <div class="abs nav-item" style="left:780px">Products<span class="caret">&#9662;</span></div>
  <div class="abs nav-item" style="left:918px">News<span class="caret">&#9662;</span></div>
  <div class="abs nav-item" style="left:1039px">Contact Us</div>
</header>

<section class="abs hero" role="img" aria-label="Landscaped park with winding path, lawns and flowering trees"></section>
<h1 class="abs hero-title">We Are Environmental Project Firm Based In Sydney Australia,<br>Working Throughout South East Asia.</h1>
<div class="abs hero-dots"><span class="on"></span><span></span><span></span><span></span></div>

<h2 class="abs welcome-title">Welcome to Tillard <em>Enviromental</em> Projects</h2>
<p class="abs welcome-lead">Lorem ipsum is simply dummy text of the printing and typesetting industry.</p>
<p class="abs welcome-copy">Lorem ipsum has been the industry's standard dummy text ever since the 1500s, when an unknown printer took a galley of type and scrambled it to make a type specimen book. it has survived not only five centuries, but also the leap into electronic typesetting, remaining essentially unchanged.</p>
<div class="abs btn welcome-btn">Read More</div>

<section class="abs mission">
  <div class="abs mv-head" style="left:88px;top:66px">
    <svg width="48" height="48" viewBox="0 0 48 48" fill="none" stroke="#fff" stroke-width="2.5"><circle cx="22" cy="26" r="18"/><circle cx="22" cy="26" r="10"/><circle cx="22" cy="26" r="3" fill="#fff"/><path d="M22 26 42 6M36 6h6v6"/></svg>
    <span>Our Mission</span>
  </div>
  <p class="abs mv-copy" style="left:90px;top:127px;width:380px">Working with people to minimise the environmental impact of humans on the earth without sacrificing lifestyle &amp; helping innovation flourish.</p>
  <div class="abs mv-more" style="left:90px;top:222px">Read More &#8594;</div>
</section>
<section class="abs vision">
  <div class="abs mv-head" style="left:146px;top:66px">
    <svg width="52" height="40" viewBox="0 0 52 40"><path d="M2 20C10 6 42 6 50 20 42 34 10 34 2 20Z" fill="#fff"/><circle cx="26" cy="20" r="9" fill="#1bb191"/><circle cx="26" cy="20" r="4" fill="#fff"/></svg>
    <span>Our Vision</span>
  </div>
  <p class="abs mv-copy" style="left:146px;top:127px;width:400px">Our Vision is to make it easy for everyone to minimise their environmental impact by providing information, technology, packaged green solutions &amp; helping innovation flourish.</p>
</section>
<div class="abs mv-badge"></div>

<section class="abs products"></section>
<h2 class="abs section-title" style="left:0;top:1486px;width:1200px;text-align:center">Our Products</h2>
<svg class="abs slider-arrow" style="left:40px;top:1728px" viewBox="0 0 20 40"><path d="M16 4 4 20l12 16" fill="none" stroke="#c9cccc" stroke-width="2"/></svg>
<svg class="abs slider-arrow" style="left:1140px;top:1728px" viewBox="0 0 20 40"><path d="M4 4l12 16L4 36" fill="none" stroke="#1bb191" stroke-width="2"/></svg>

<article class="abs product-card" style="left:90px">
  <div class="pic" role="img" aria-label="Assorted fresh vegetables" style="background:linear-gradient(135deg,#5e9a2f,#c9472b 55%,#e49a2c)"></div>
  <h3>Sustainable Food</h3>
  <p>Duis autem vel eum iriure dolor in morek ol hendrerit inknl vulputate velit facilisis.</p>
  <div class="plus">+</div>
</article>
<article class="abs product-card" style="left:441px">
  <div class="pic" role="img" aria-label="Vertical green wall beside a walkway" style="background:linear-gradient(180deg,#7fa0c4,#4f7a32 45%,#6d8a3c)"></div>
  <h3>Green Walls</h3>
  <p>Duis autem vel eum iriure dolor in morek ol hendrerit inknl vulputate velit facilisis.</p>
  <div class="plus">+</div>
</article>
<article class="abs product-card" style="left:791px">
  <div class="pic" role="img" aria-label="Landscaped eco garden with circular flower bed" style="background:linear-gradient(180deg,#3c7ec8,#8fc0e6 40%,#5aa03a 60%,#4a8a2c)"></div>
  <h3>Eco Gardens</h3>
  <p>Duis autem vel eum iriure dolor in morek ol hendrerit inknl vulputate velit facilisis.</p>
  <div class="plus">+</div>
</article>
<div class="abs btn" style="left:528px;top:1967px;width:142px;height:34px;line-height:34px">View All</div>

<h2 class="abs section-title" style="left:90px;top:2152px">Our Projects</h2>
<div class="abs" role="img" aria-label="Greenhouse with rows of young crops" style="left:90px;top:2225px;width:494px;height:202px;background:linear-gradient(180deg,#8a9a8a,#5a8c3a 40%,#3f7028)"></div>
<div class="abs" role="img" aria-label="Crop field at dusk" style="left:90px;top:2436px;width:239px;height:200px;background:linear-gradient(180deg,#35506a,#3d4a2e 60%,#2e3a22)"></div>
<div class="abs proj-caption"><b>DOLLAR CONSEQUTE</b><span>Duis autem vel eum iriure dolor hendrerit inknl vulputat. [+]</span></div>
<div class="abs" role="img" aria-label="Hydroponic growing racks with leafy plants" style="left:338px;top:2436px;width:246px;height:200px;background:linear-gradient(135deg,#d7dcd6,#7fae5a 55%,#dfe3de)"></div>
<div class="abs btn" style="left:90px;top:2670px;width:141px;height:34px;line-height:34px">View All</div>

<h2 class="abs section-title" style="left:616px;top:2152px">Latest Events</h2>
<div class="abs tab" style="left:623px;width:80px;background:#c9cccc">Blogposts</div>
<div class="abs tab" style="left:713px;width:105px;background:var(--teal)">Latest News</div>
<div class="abs" style="left:1000px;top:2232px;font-size:14px;color:var(--ink)">View All</div>
<svg class="abs" style="left:1108px;top:2268px" width="4" height="360"><rect width="2" height="360" fill="#e2e4e4"/><rect width="2" height="90" fill="#bfc3c3"/></svg>

<div class="abs event" style="top:2278px"><div class="date"><b>26</b><i>Dec</i></div><h4>Consectetuer Adipiscing</h4><p>Lorem ipsum dolor sit amet, consectetuer adipiscing elit, sed di nonummy nibh euismod tincidunt ut laoreet dolore manos...</p></div>
<div class="abs event" style="top:2366px"><div class="date"><b>28</b><i>Dec</i></div><h4>Consectetuer Adipiscing</h4><p>Lorem ipsum dl.orem ipsum dolor sit amet, consectetuer adipiscing elit, sed di nonummy nibh euismod tincidunt ut laoreet dolore...</p></div>
<div class="abs event" style="top:2454px"><div class="date"><b>02</b><i>Jan</i></div><h4>Consectetuer Adipiscing</h4><p>Lorem ipsum dolor sit amet, consectetuer adipiscing elit, sed di nonummy nibh euismod tincidunt ut laoreet dolore manos...</p></div>
<div class="abs event" style="top:2541px"><div class="date"><b>04</b><i>Jan</i></div><h4>Consectetuer Adipiscing</h4><p>Lorem ipsum dolor sit amet, consectetuer adipiscing elit, sed di nonummy nibh euismod tincidunt ut laoreet dolore manos...</p></div>
<svg class="abs" style="left:856px;top:2625px" width="16" height="10"><path d="M2 2l6 6 6-6" fill="none" stroke="#999" stroke-width="1.5"/></svg>

<section class="abs testimonials" role="img" aria-label="Aquaculture tanks in an outdoor facility"></section>
<h2 class="abs testi-title">Client <em>Testimonials</em></h2>
<p class="abs testi-copy">Lorem ipsum dolor sit amet, consectetuer adipiscing elit, sed diam nonummy nibh euismod tincidunt ut laoreet dolore magna aliquam erat volutpat. Ut wisi enim ad minim veniam, quis nostrud exerci tation ullamcorper suscipit lobortis nisl ut aliquip ex ea commodo consequat. Duis autem vel eum iriure dolor in hendrerit in vulputate velit esse molestie consequat, vel illum dolore eu feugiat nulla facilisis at vero eros et accumsan et iusto</p>
<svg class="abs slider-arrow" style="left:82px;top:2960px" viewBox="0 0 20 40"><path d="M16 4 4 20l12 16" fill="none" stroke="#fff" stroke-width="2"/></svg>
<svg class="abs slider-arrow" style="left:1098px;top:2960px" viewBox="0 0 20 40"><path d="M4 4l12 16L4 36" fill="none" stroke="#fff" stroke-width="2"/></svg>
<div class="abs avatar" role="img" aria-label="Client portrait" style="left:474px"></div>
<div class="abs avatar on" role="img" aria-label="Client portrait" style="left:566px"></div>
<div class="abs avatar" role="img" aria-label="Client portrait" style="left:656px"></div>
<div class="abs testi-name">Lorem Ipsum</div>

<footer class="abs site-footer"></footer>
<h3 class="abs foot-head" style="left:90px">Contact Details</h3>
<h3 class="abs foot-head" style="left:433px">Location Map</h3>
<svg class="abs foot-icon" style="top:3376px" width="18" height="24" viewBox="0 0 18 24"><path d="M9 1a8 8 0 0 0-8 8c0 6 8 14 8 14s8-8 8-14a8 8 0 0 0-8-8z" fill="#fff"/><circle cx="9" cy="9" r="3" fill="#1bb191"/></svg>
<div class="abs foot-line" style="top:3372px;font-weight:500">Tillardenv Environmental</div>
<div class="abs foot-line" style="top:3394px">123, Lorem Ipsum Dolor way,</div>
<div class="abs foot-line" style="top:3416px">consectet, CA 123456</div>
<svg class="abs foot-icon" style="top:3457px" width="18" height="18" viewBox="0 0 18 18"><path d="M4 1l3 4-2 2c1 2 3 4 5 5l2-2 4 3-2 3C8 16 2 10 1 4z" fill="#fff"/></svg>
<div class="abs foot-line" style="top:3455px">123 456 7890</div>
<svg class="abs foot-icon" style="top:3498px" width="20" height="16" viewBox="0 0 20 16"><rect x="1" y="1" width="18" height="14" fill="none" stroke="#fff" stroke-width="1.8"/><path d="M1 1l9 7 9-7" fill="none" stroke="#fff" stroke-width="1.8"/></svg>
<div class="abs foot-line" style="top:3496px">inquiry@tillardenv.com</div>
<div class="abs map" role="img" aria-label="Street map with location pin"></div>
<svg class="abs" style="left:568px;top:3418px" width="26" height="34" viewBox="0 0 18 24"><path d="M9 1a8 8 0 0 0-8 8c0 6 8 14 8 14s8-8 8-14a8 8 0 0 0-8-8z" fill="#e0463a"/><circle cx="9" cy="9" r="3" fill="#fff"/></svg>
<div class="abs foot-brand"><span class="mark"></span><span class="name">Tillard Environmental Projects</span></div>

<div class="abs bottom-bar">
  <div class="abs copyright">Copyright &copy; 2019 Tillard Environmental. All Rights Reserved.</div>
  <div class="abs socials"><span></span><span></span><span></span><span></span></div>
</div>

</body>
</html>
```